we need a business card as well as a logo that can be used for signs etc.
this is a very formal, classy , elegant function centre, as well as café. I am after a design that stands out and grabs people attentions. my colours theme is really warm ,colours like chocolate browns, and latte type colours with really deep red tones
not bright red, just warm tones. this is a place that very wealthy and maybe even celebs will come so I need it to be appealing.
Industry/Entity Type
Business
Contact Information for Business Card
Blue Fern
café and function centre @ hallam orchard.
wedding and function specialists,
Barrow parkway, millbrook,ph 0438157240

```html
<!DOCTYPE html>
<html lang="en">
<head>
<meta charset="utf-8">
<title>Blue Fern café – business card</title>
<link rel="stylesheet" href="https://fonts.googleapis.com/css2?family=Allura&family=Dosis:wght@400;500&display=swap">
<style>
  :root {
    --page: #ffffff;
    --card-top: #ffffff;
    --pattern-light: #f7f4f2;
    --pattern-mid: #e8e1dd;
    --wine: #521416;
    --script-ink: #5a1a1e;
    --cocoa: #5d4e47;
    --cream: #ffffff;
  }
  * { margin: 0; padding: 0; box-sizing: border-box; }
  html, body {
    width: 1000px;
    height: 1200px;
    overflow: hidden;
    background: var(--page);
  }
  .canvas {
    position: relative;
    width: 1000px;
    height: 1200px;
  }
  .business-card {
    position: absolute;
    left: 152px;
    top: 370px;
    width: 736px;
    height: 492px;
    background: var(--card-top);
    overflow: hidden;
  }
  .swirl-backdrop {
    position: absolute;
    left: 0;
    top: 0;
    width: 736px;
    height: 325px;
    background: radial-gradient(ellipse at 40% 50%, var(--pattern-light) 0%, var(--pattern-mid) 100%);
  }
  .brand-block {
    position: absolute;
    left: 0;
    top: 0;
    width: 470px;
    height: 325px;
    font-family: "Allura", cursive;
    color: var(--script-ink);
  }
  .brand-name {
    position: absolute;
    left: 26px;
    top: 112px;
    font-size: 57px;
    line-height: 1;
    white-space: nowrap;
  }
  .brand-descriptor {
    position: absolute;
    left: 56px;
    top: 170px;
    font-size: 57px;
    line-height: 1;
    white-space: nowrap;
  }
  .brand-location {
    position: absolute;
    left: 148px;
    top: 222px;
    font-size: 40px;
    line-height: 1;
    white-space: nowrap;
  }
  .brand-disc {
    position: absolute;
    left: 468px;
    top: 79px;
  }
  .info-band {
    position: absolute;
    left: 0;
    top: 325px;
    width: 736px;
    height: 167px;
    background: var(--wine);
    color: var(--cream);
    font-family: "Dosis", sans-serif;
  }
  .tagline {
    position: absolute;
    left: 26px;
    top: 45px;
    font-size: 37px;
    font-weight: 400;
    white-space: nowrap;
  }
  .contact {
    position: absolute;
    left: 500px;
    top: 20px;
    width: 230px;
    text-align: center;
    font-size: 28px;
    line-height: 36px;
    font-weight: 400;
    font-style: normal;
  }
</style>
</head>
<body>
<main class="canvas">
  <section class="business-card">
    <div class="swirl-backdrop" role="img" aria-label="Ornamental swirling flourish pattern in soft latte tones"></div>

    <div class="brand-block">
      <p class="brand-name">Blue Fern café</p>
      <p class="brand-descriptor">and function centre</p>
      <p class="brand-location">@ hallam orchard.</p>
    </div>

    <svg class="brand-disc" width="214" height="214" viewBox="0 0 214 214" aria-hidden="true">
      <circle cx="107" cy="107" r="106" fill="var(--cocoa)"/>
    </svg>

    <div class="info-band">
      <p class="tagline">wedding and function specialists,</p>
      <address class="contact">
        Barrow parkway,<br>
        millbrook,<br>
        ph 0438157240
      </address>
    </div>
  </section>
</main>
</body>
</html>
```